Digital Marketing Brochure - PDF

I am seeking to have a digital marketing brochure consistent with our webpage of birchwellgroup.com that includes our staff, territory and will have available links to a share file for our insurance documents and rates, etc. - I have uploaded our logo and would like you work with our webpage to keep consistent. We would like this to be a pdf style document that reads like a book and has pleasing modern, rustic appearance consistent with our web page.

Target Market(s)

Insurance companies

Industry/Entity Type

Insurance

Requirements
Must have
• Flip through marketing brochure. Essentially want it to be our webpage in a e-mailable or downloadable pdf.

```html
<!DOCTYPE html>
<html lang="en">
<head>
<meta charset="utf-8">
<title>Birchwell Brochure – Cover Spread</title>
<link rel="stylesheet" href="https://fonts.googleapis.com/css2?family=Montserrat:wght@400;600;700;800;900&family=Open+Sans:wght@300;400;600;700&display=swap">
<style>
  :root {
    --navy: #1c3864;
    --navy-deep: #142a4d;
    --orange: #e8561b;
    --paper: #f4f4f4;
    --white: #ffffff;
    --photo-dark: #2a1c1c;
    --photo-mid: #6a2f22;
    --photo-hot: #c8481d;
  }
  * { box-sizing: border-box; margin: 0; padding: 0; }
  html, body { width: 1200px; height: 824px; overflow: hidden; background: #2b2b2b; }
  body { font-family: "Open Sans", Arial, sans-serif; }

  .spread { position: relative; width: 1200px; height: 824px; background: var(--paper); }
  .page { position: absolute; top: 0; width: 600px; height: 824px; }
  .page--back { left: 0; }
  .page--front { left: 600px; }
  .spine {
    position: absolute; left: 594px; top: 0; width: 12px; height: 824px;
    background: linear-gradient(90deg, rgba(0,0,0,0) 0%, rgba(0,0,0,.12) 50%, rgba(0,0,0,0) 100%);
    z-index: 5;
  }

  /* shared photo across both pages */
  .cover-photo {
    position: absolute; left: 300px; top: 180px; width: 840px; height: 450px;
    background:
      radial-gradient(ellipse at 18% 30%, rgba(232,110,30,.85) 0%, rgba(200,72,29,.4) 25%, rgba(0,0,0,0) 50%),
      radial-gradient(ellipse at 82% 18%, rgba(200,60,30,.7) 0%, rgba(0,0,0,0) 45%),
      radial-gradient(ellipse at 60% 70%, rgba(120,110,60,.5) 0%, rgba(0,0,0,0) 50%),
      linear-gradient(160deg, var(--photo-mid) 0%, var(--photo-dark) 55%, #3a1a14 100%);
  }
  .cover-photo__shade {
    position: absolute; inset: 0;
    background: linear-gradient(180deg, rgba(20,10,10,.35) 0%, rgba(0,0,0,0) 35%, rgba(0,0,0,0) 70%, rgba(90,30,15,.55) 100%);
  }

  /* back page */
  .back-title {
    position: absolute; left: 60px; top: 70px; width: 420px;
    font-family: "Montserrat", Arial, sans-serif; font-weight: 700;
    font-size: 25px; line-height: 1.25; color: var(--orange);
  }
  .service-panel {
    position: absolute; left: 0; top: 180px; width: 330px; height: 520px;
    background: linear-gradient(90deg, var(--navy) 0%, var(--navy) 78%, rgba(28,56,100,0) 100%);
    color: var(--white);
    padding: 60px 30px 0 60px;
  }
  .service-panel__heading {
    font-family: "Montserrat", Arial, sans-serif; font-weight: 800;
    font-size: 17px; line-height: 1.25; text-transform: uppercase; letter-spacing: .5px;
  }
  .service-panel__text { font-size: 15px; line-height: 1.45; font-weight: 400; width: 250px; }
  .home-office { margin-top: 70px; margin-left: 60px; }
  .home-office__label {
    font-size: 13px; display: inline-block; padding-bottom: 4px;
    border-bottom: 2px solid var(--orange);
  }
  .home-office__label b { font-weight: 700; }
  .contact-line { display: flex; align-items: flex-start; gap: 10px; font-size: 13px; line-height: 1.35; margin-top: 8px; }
  .contact-line svg { flex: none; margin-top: 2px; }
  .contact-line--strong { font-weight: 700; }
  .contact-line--first { margin-top: 16px; }

  .web-bar {
    position: absolute; height: 34px; background: var(--orange); color: var(--white);
    display: flex; align-items: center; gap: 10px; font-size: 14px;
  }
  .web-bar b { font-weight: 700; }
  .web-bar__tab { position: absolute; right: -8px; top: 0; width: 8px; height: 100%; background: var(--navy); }
  .web-bar--back { left: 0; top: 745px; width: 440px; padding-left: 60px; }
  .web-bar--front { left: 230px; top: 640px; width: 370px; padding-left: 20px; }
  .web-bar--front .web-bar__tab { left: -8px; right: auto; }

  /* front page */
  .since-tab {
    position: absolute; left: 30px; top: 30px; width: 34px; height: 120px;
    background: var(--navy); color: var(--white);
    display: flex; align-items: center; justify-content: center;
  }
  .since-tab span {
    transform: rotate(-90deg); white-space: nowrap;
    font-family: "Montserrat", Arial, sans-serif; font-weight: 700; font-size: 13px; letter-spacing: 1px;
  }
  .brand { position: absolute; right: 60px; top: 60px; text-align: right; }
  .brand__name {
    display: flex; align-items: center; gap: 10px; justify-content: flex-end;
    font-family: "Montserrat", Arial, sans-serif; font-weight: 900; font-size: 46px; line-height: 1;
    color: var(--orange); letter-spacing: 1px;
  }
  .brand__dot { width: 16px; height: 16px; border-radius: 50%; background: var(--orange); }
  .brand__tagline { margin-top: 6px; font-size: 11px; color: var(--navy); text-transform: uppercase; letter-spacing: .4px; }

  .hazards {
    position: absolute; right: 80px; top: 220px; text-align: right;
    font-family: "Montserrat", Arial, sans-serif; font-weight: 700; font-size: 17px; line-height: 1.35;
    color: var(--white); text-transform: uppercase; letter-spacing: .3px;
  }
  .slogan {
    position: absolute; right: 80px; top: 565px;
    font-family: "Montserrat", Arial, sans-serif; font-size: 32px; color: var(--white); text-transform: uppercase;
  }
  .slogan__light { font-weight: 400; }
  .slogan__bold { font-weight: 800; }

  .hotline {
    position: absolute; left: 330px; top: 690px; width: 240px;
    display: flex; align-items: center; gap: 10px;
    font-family: "Montserrat", Arial, sans-serif; font-weight: 700; font-size: 19px; color: var(--navy);
  }
  .hotline__rule { position: absolute; left: 320px; top: 726px; width: 280px; height: 5px; background: var(--navy); }
</style>
</head>
<body>
<main class="spread">

  <div class="cover-photo" role="img" aria-label="Photograph of firefighters in turnout gear and air tanks working in front of a burning building">
    <div class="cover-photo__shade"></div>
  </div>

  <section class="page page--back">
    <h2 class="back-title">Independent Claim Adjusters &amp; Administration</h2>

    <div class="service-panel">
      <h3 class="service-panel__heading">Serving you<br>from 12 locations</h3>
      <p class="service-panel__text">throughout the North East, with claim staff throughout the region, BIRCHWELL has the resources to respond to your adjustment needs.</p>
    </div>

    <div class="home-office" style="position:absolute;left:0;top:460px;color:var(--white);">
      <div class="home-office__label">Home <b>Office</b></div>
      <div class="contact-line contact-line--first">
        <svg width="12" height="16" viewBox="0 0 12 16"><path d="M6 1a5 5 0 0 0-5 5c0 4 5 9 5 9s5-5 5-9a5 5 0 0 0-5-5z" fill="none" stroke="#e8561b" stroke-width="1.6"/><circle cx="6" cy="6" r="1.8" fill="#e8561b"/></svg>
        <span>PO Box 219<br>410 Millbrook Road<br>Halden Park, NY 12099</span>
      </div>
      <div class="contact-line contact-line--strong">
        <svg width="14" height="14" viewBox="0 0 14 14"><circle cx="7" cy="7" r="6" fill="none" stroke="#e8561b" stroke-width="1.4"/><path d="M4.5 4c.3 2.5 2.5 5 5 5.5l.8-1.2-1.5-.8-.7.6c-.9-.4-1.6-1.1-2-2l.6-.7-.8-1.5z" fill="#e8561b"/></svg>
        <span>518-555-0142</span>
      </div>
      <div class="contact-line">
        <svg width="14" height="14" viewBox="0 0 14 14"><rect x="3" y="1" width="8" height="4" fill="none" stroke="#e8561b" stroke-width="1.3"/><rect x="1" y="5" width="12" height="5" rx="1" fill="#e8561b"/><rect x="3.5" y="9" width="7" height="4" fill="none" stroke="#e8561b" stroke-width="1.3"/></svg>
        <span>888-555-0178</span>
      </div>
      <div class="contact-line contact-line--strong">
        <svg width="14" height="14" viewBox="0 0 14 14"><circle cx="7" cy="7" r="6" fill="none" stroke="#e8561b" stroke-width="1.4"/><path d="M4.5 4c.3 2.5 2.5 5 5 5.5l.8-1.2-1.5-.8-.7.6c-.9-.4-1.6-1.1-2-2l.6-.7-.8-1.5z" fill="#e8561b"/></svg>
        <span>1-800-555-0136</span>
      </div>
    </div>

    <div class="web-bar web-bar--back">
      <svg width="16" height="16" viewBox="0 0 16 16"><g fill="none" stroke="#fff" stroke-width="1.3"><circle cx="8" cy="8" r="6.5"/><ellipse cx="8" cy="8" rx="3" ry="6.5"/><path d="M1.5 8h13M2.5 5h11M2.5 11h11"/></g></svg>
      <span>www.<b>birchwellgroup</b>.com</span>
      <div class="web-bar__tab"></div>
    </div>
  </section>

  <div class="spine"></div>

  <section class="page page--front">
    <div class="since-tab"><span>SINCE 1980</span></div>

    <div class="brand">
      <div class="brand__name"><span class="brand__dot"></span>BIRCHWELL</div>
      <div class="brand__tagline">Birchwell Claims &amp; Adjusting Services</div>
    </div>

    <h1 class="hazards">Accidents, Disasters, Fire,<br>Flood, Wind, Property &amp; Liability</h1>

    <p class="slogan"><span class="slogan__light">When it </span><span class="slogan__bold">Happens</span></p>

    <div class="web-bar web-bar--front">
      <div class="web-bar__tab"></div>
      <svg width="16" height="16" viewBox="0 0 16 16"><g fill="none" stroke="#fff" stroke-width="1.3"><circle cx="8" cy="8" r="6.5"/><ellipse cx="8" cy="8" rx="3" ry="6.5"/><path d="M1.5 8h13M2.5 5h11M2.5 11h11"/></g></svg>
      <span>www.<b>birchwellgroup</b>.com</span>
    </div>

    <div class="hotline">
      <svg width="18" height="18" viewBox="0 0 14 14"><circle cx="7" cy="7" r="6" fill="none" stroke="#e8561b" stroke-width="1.4"/><path d="M4.5 4c.3 2.5 2.5 5 5 5.5l.8-1.2-1.5-.8-.7.6c-.9-.4-1.6-1.1-2-2l.6-.7-.8-1.5z" fill="#e8561b"/></svg>
      <span>1-800-555-0136</span>
    </div>
    <div class="hotline__rule"></div>
  </section>

</main>
</body>
</html>
```